Pura Senda Trek Holidays Rack Card

We need a double sided rack card design. One side should be promoting our "Seven Trail Days" tour with the flip side promoting our "Honeymoon" and "Custom & Family Tours". Colours should be in line with our website www.PuraSendaTrek.example. Text and photos attached (feel free to use as necessary). We are looking for a fun rack card that will catch clients eyes and hopefully promote Costa Rica as a fun and exciting vacation.

Target Market(s)

Tourism - USA and Canada

Industry/Entity Type

Tourism

Font styles to use
Sans Serif

Colors
0455a3
33a6d7
f37122

Requirements
Must have
• Our logo on both sides of the rack card. Must be bright and fun looking. Costa Rica is an outdoor destination with tons of fun activities to do, we want to try and get that feeling across on the card.
Nice to have
• I have added a price sticker to the attachments on this project. Is it possible to have something similar on the Seven Trail Days side? The price would be $1999 scored out with the new price being $1649.

```html
<!DOCTYPE html>
<html lang="en">
<head>
<meta charset="utf-8">
<title>Pura Senda Trek Holidays – Rack Card</title>
<link href="https://fonts.googleapis.com/css2?family=Lobster&family=Kalam:wght@400;700&family=Open+Sans:wght@400;600&display=swap" rel="stylesheet">
<style>
:root{
  --navy:#0455a3;
  --sky:#33a6d7;
  --sky-light:#7fd0f0;
  --orange:#f37122;
  --orange-soft:#f79a3a;
  --red:#d5192a;
  --white:#ffffff;
  --ink:#1d2f45;
  --stage:#e9e4dc;
}
*{box-sizing:border-box;margin:0;padding:0}
html,body{width:1200px;height:1000px;overflow:hidden;background:var(--stage)}
.canvas{position:relative;width:1200px;height:1000px}
.rack-card{position:absolute;top:50px;width:432px;height:900px;overflow:hidden;
  background:linear-gradient(180deg,#8fd6f4 0%,var(--sky) 55%,#2f8fd0 100%);
  box-shadow:0 6px 18px rgba(0,0,0,.25)}
.rack-card--front{left:130px}
.rack-card--back{left:638px}
.photo{position:absolute}
.polaroid{position:absolute;background:var(--white);padding:6px 6px 16px;box-shadow:0 3px 8px rgba(0,0,0,.3)}
.polaroid .photo{position:static;width:100%;height:100%}

/* front */
.title-banner{position:absolute;left:14px;top:16px;width:382px;height:86px;background:var(--orange);
  border-radius:8px 14px 6px 12px;transform:rotate(-1deg);text-align:center;color:var(--white)}
.title-banner h1{font-family:"Lobster",cursive;font-weight:400;font-size:38px;line-height:1;margin-top:10px}
.title-banner p{font-family:"Lobster",cursive;font-size:21px;letter-spacing:.5px;margin-top:4px}
.landscape{left:0;top:110px;width:432px;height:290px;
  background:linear-gradient(180deg,#9ccbe6 0%,#5f8f4a 35%,#2f6b2a 70%,#5b7a60 100%)}
.itinerary-tab{position:absolute;left:0;top:374px;width:122px;height:38px;background:var(--navy);
  font-family:"Lobster",cursive;color:var(--white);font-size:27px;padding-left:16px;line-height:38px}
.itinerary{position:absolute;left:18px;top:425px;list-style:none}
.itinerary li{display:flex;align-items:center;height:40px}
.day-badge{width:28px;height:28px;border-radius:50%;background:var(--orange);color:var(--white);
  font-family:"Kalam",cursive;text-align:center;line-height:1;padding-top:3px;margin-right:12px;flex:none}
.day-badge small{display:block;font-size:9px}
.day-badge b{display:block;font-size:15px}
.itinerary span.activity{font-family:"Kalam",cursive;color:var(--white);font-size:16px;line-height:1.05;
  text-shadow:0 1px 2px rgba(0,40,90,.4)}
.price-tag{position:absolute;left:300px;top:478px;width:135px;height:210px}
.invite{position:absolute;left:0;top:738px;width:432px;text-align:center;font-family:"Kalam",cursive;
  font-weight:700;color:var(--orange-soft);font-size:16px;line-height:24px;font-style:italic}

/* footer */
.card-footer{position:absolute;left:0;bottom:0;width:432px;height:92px;background:var(--white)}
.contact{position:absolute;left:22px;top:10px;list-style:none;font-family:"Open Sans",sans-serif;font-size:13px;color:var(--ink)}
.contact li{display:flex;align-items:center;height:24px}
.contact svg{width:14px;height:14px;margin-right:10px;fill:var(--navy)}
.brand{position:absolute;right:24px;top:28px;display:flex;align-items:center}
.brand-name{font-family:"Open Sans",sans-serif;font-weight:600;font-size:22px;color:var(--sky)}
.brand-dot{width:16px;height:16px;border-radius:50%;background:var(--navy);margin-left:8px}

/* back */
.sunset{left:0;top:0;width:432px;height:240px;
  background:linear-gradient(180deg,#c46a5a 0%,#f08a4c 45%,#f0a06a 62%,#7fb9d6 85%,#8fd6f4 100%)}
.back-title{position:absolute;right:22px;top:128px;text-align:right;font-family:"Lobster",cursive;
  color:var(--white);font-size:31px;line-height:42px;text-shadow:0 2px 3px rgba(0,40,90,.45)}
.about{position:absolute;left:24px;top:250px;width:248px;font-family:"Kalam",cursive;font-size:14px;
  line-height:22.5px;color:var(--ink)}
.tagline{position:absolute;left:18px;top:566px;font-family:"Kalam",cursive;font-weight:700;font-size:30px;line-height:40px;color:var(--ink)}
.beach{left:0;top:610px;width:432px;height:198px;
  background:linear-gradient(180deg,#4fb8d4 0%,#9fd8dc 30%,#efe0c8 55%,#e8bfa0 100%)}
</style>
</head>
<body>
<div class="canvas">

  <section class="rack-card rack-card--front">
    <div class="photo landscape" role="img" aria-label="Green volcano and rainforest with a rock waterfall pool"></div>
    <div class="title-banner">
      <h1>Seven Trail Days</h1>
      <p>8 Days, 8 Adventures, 1 Life</p>
    </div>

    <div class="polaroid" style="left:130px;top:295px;width:108px;height:104px;transform:rotate(-5deg)">
      <div class="photo" role="img" aria-label="Group whitewater rafting" style="background:linear-gradient(160deg,#6b9ac0,#2e4e7a,#b8d3e6)"></div>
    </div>
    <div class="polaroid" style="left:235px;top:302px;width:106px;height:104px;transform:rotate(2deg)">
      <div class="photo" role="img" aria-label="Snorkelers underwater" style="background:linear-gradient(180deg,#3cc0e0,#1583b8)"></div>
    </div>
    <div class="polaroid" style="left:330px;top:312px;width:104px;height:104px;transform:rotate(6deg)">
      <div class="photo" role="img" aria-label="Canyoning down a waterfall" style="background:linear-gradient(160deg,#5d8a4e,#c9d9c0,#3f6a3a)"></div>
    </div>

    <div class="itinerary-tab">Itinerary</div>

    <ol class="itinerary">
      <li><span class="day-badge"><small>Day</small><b>1</b></span><span class="activity">Pick Up San Jose International Airport</span></li>
      <li><span class="day-badge"><small>Day</small><b>2</b></span><span class="activity">Beginner Kayaking</span></li>
      <li><span class="day-badge"><small>Day</small><b>3</b></span><span class="activity">Whitewater Rafting. Overnight Jungle Lodge</span></li>
      <li><span class="day-badge"><small>Day</small><b>4</b></span><span class="activity">Canopy/Zipline Tour &amp; Jungle Hikes.<br>Overnight Jungle Lodge</span></li>
      <li><span class="day-badge"><small>Day</small><b>5</b></span><span class="activity">Whitewater Rafting &amp; Beach</span></li>
      <li><span class="day-badge"><small>Day</small><b>6</b></span><span class="activity">Surfing &amp; Snorkeling</span></li>
      <li><span class="day-badge"><small>Day</small><b>7</b></span><span class="activity">Canyoning (Rappelling Waterfalls) or<br>Mountain Biking. Your choice!</span></li>
      <li><span class="day-badge"><small>Day</small><b>8</b></span><span class="activity">Drop Off San Jose International Airport</span></li>
    </ol>

    <svg class="price-tag" viewBox="0 0 135 210" aria-label="Price $1999, special promotion price $1649">
      <path d="M120 0 C132 20 118 40 98 52" fill="none" stroke="#444" stroke-width="2"/>
      <g transform="rotate(22 70 120)">
        <path d="M50 48 L92 48 L108 72 L108 196 L34 196 L34 72 Z" fill="var(--red)" stroke="#a10f1c" stroke-width="1.5"/>
        <circle cx="71" cy="66" r="5" fill="#f4f4f4"/>
        <g font-family="Kalam, cursive" fill="#fff" text-anchor="middle">
          <text x="71" y="98" font-size="13">Price <tspan text-decoration="line-through">$1999</tspan></text>
          <text x="71" y="116" font-size="13">Special</text>
          <text x="71" y="133" font-size="13">Promotion</text>
          <text x="71" y="150" font-size="13">Price</text>
          <text x="71" y="180" font-size="24" font-weight="700">$1649</text>
        </g>
      </g>
    </svg>

    <p class="invite">Come join us in the tropics on one of our<br>all inclusive 8 day Seven Trail Days tours.</p>

    <footer class="card-footer">
      <ul class="contact">
        <li><svg viewBox="0 0 16 16"><path d="M1 3h14v10H1z M1 3l7 6 7-6" /></svg>info@PuraSendaTrek.example</li>
        <li><svg viewBox="0 0 16 16"><path d="M4 1l3 3-2 2c1 2 3 4 5 5l2-2 3 3-2 3C7 14 2 9 1 3z"/></svg>1-888-555-0142</li>
        <li><svg viewBox="0 0 16 16"><circle cx="8" cy="8" r="7"/></svg>www.PuraSendaTrek.example</li>
      </ul>
      <div class="brand"><span class="brand-name">Pura Senda</span><span class="brand-dot"></span></div>
    </footer>
  </section>

  <section class="rack-card rack-card--back">
    <div class="photo sunset" role="img" aria-label="Couple walking hand in hand on the beach at sunset"></div>
    <h2 class="back-title">Honeymoons &amp;<br>Custom and Family Tours</h2>

    <p class="about">Pura Senda has been specializing in helping plan unique tropical getaways since 1995. Based in Costa Rica 365 days a year, we are able to recommend the best activities, hotels and destinations to suit your vacation/ honeymoon desires. We have personally explored and enjoyed many of the region’s attractions and know which ones will give you the best experience while you are here. Let us know what you are looking for and we’ll come up with an incredible itinerary,</p>
    <p class="tagline">just for you!</p>

    <div class="photo beach" role="img" aria-label="Sandy feet on the beach by the sea"></div>

    <div class="polaroid" style="left:294px;top:222px;width:132px;height:130px;transform:rotate(3deg)">
      <div class="photo" role="img" aria-label="Woman on a zipline in the jungle" style="background:linear-gradient(160deg,#3f7a36,#8cb86a,#2d5a2a)"></div>
    </div>
    <div class="polaroid" style="left:292px;top:356px;width:130px;height:130px;transform:rotate(2deg)">
      <div class="photo" role="img" aria-label="Sloth hanging in a tree" style="background:linear-gradient(160deg,#8ab84a,#9a8060,#4f7a2c)"></div>
    </div>
    <div class="polaroid" style="left:284px;top:488px;width:134px;height:142px;transform:rotate(-2deg)">
      <div class="photo" role="img" aria-label="Children in snorkel masks at the beach" style="background:linear-gradient(180deg,#7fc8e8,#f0c8a8,#e85a7a)"></div>
    </div>

    <footer class="card-footer">
      <ul class="contact">
        <li><svg viewBox="0 0 16 16"><path d="M1 3h14v10H1z M1 3l7 6 7-6" /></svg>info@PuraSendaTrek.example</li>
        <li><svg viewBox="0 0 16 16"><path d="M4 1l3 3-2 2c1 2 3 4 5 5l2-2 3 3-2 3C7 14 2 9 1 3z"/></svg>1-888-555-0142</li>
        <li><svg viewBox="0 0 16 16"><circle cx="8" cy="8" r="7"/></svg>www.PuraSendaTrek.example</li>
      </ul>
      <div class="brand"><span class="brand-name">Pura Senda</span><span class="brand-dot"></span></div>
    </footer>
  </section>

</div>
</body>
</html>
```